KRM RFP Powerpoint Template -

Kestrel Resonance Media. I need an RFP design template that reflects our business...audio, video staging, and lighting for corporate events. Our website is krmstage.com. Added a title page we came up with...includes our logo and a 3 bar theme

Target Market(s)

Medium and large business that have events

Industry/Entity Type

Event entertainer

Font styles to use
Other font styles liked:
• Calibri

Colors
0094D4
00A9DD
6FCCEA
C7EBF8
E9F6FB
59FF00
82FF00
B8FF75
E3FFCB
F4FFEA

Requirements
Must have
• A solid template design that reflects the excitement and energy of a large event
Nice to have
• Lots of graphics that can be manipulated. Pictures of concert type lights. Video walls, speaker arrays. A consistent look and feel. Template designs for entering financial info into tables

```html
<!DOCTYPE html>
<html lang="en">
<head>
<meta charset="utf-8">
<title>KRM RFP Template</title>
<link href="https://fonts.googleapis.com/css2?family=Carlito:wght@400;700&display=swap" rel="stylesheet">
<style>
:root{
  --blue:#0094D4;
  --blue-2:#00A9DD;
  --blue-3:#6FCCEA;
  --blue-4:#C7EBF8;
  --blue-5:#E9F6FB;
  --ink:#1b1b1b;
  --text:#555b61;
  --canvas:#eef0f3;
  --photo-dark:#0d1a33;
  --photo-mid:#26306a;
}
*{box-sizing:border-box;margin:0;padding:0}
html,body{width:1200px;height:3868px;overflow:hidden}
body{background:var(--canvas);font-family:"Carlito",Calibri,Arial,sans-serif;color:var(--ink)}
.deck{position:relative;width:1200px;height:3868px;padding-top:100px}
.slide{position:relative;width:1000px;height:562px;margin:0 auto 58px;background:#fff;box-shadow:0 2px 8px rgba(0,0,0,.08);overflow:hidden}
.photo{position:absolute;background:linear-gradient(160deg,var(--photo-mid),var(--photo-dark) 60%,#3a1a4a)}
.slide-footer{position:absolute;left:0;right:0;bottom:0;height:22px;background:var(--blue);color:#fff;font-size:10px;display:flex;justify-content:space-between;align-items:center;padding:0 24px}
.slide-footer::before{content:"";position:absolute;left:0;right:0;top:-4px;height:2px;background:var(--blue-3)}
.brand{font-weight:700;font-size:58px;letter-spacing:1px;color:var(--ink);line-height:1}
.slide-title{font-size:40px;font-weight:700;text-align:center;padding-top:44px}

/* cover */
.cover .photo{left:0;top:0;width:340px;height:100%}
.cover .brand{position:absolute;right:60px;top:70px}
.cover .intro{position:absolute;left:440px;right:60px;top:220px;text-align:right}
.cover .intro h2{font-size:24px;font-weight:700}
.cover .intro h1{font-size:44px;font-weight:700;line-height:1.05;margin-top:4px}
.cover .intro p{font-size:12px;color:var(--text);margin-top:14px;line-height:1.4}
.cover .next{position:absolute;right:60px;top:430px;width:24px;height:24px;border-radius:50%;background:var(--blue)}
.cover .bar{position:absolute;left:0;right:0;bottom:0;height:6px;background:var(--blue)}

/* services */
.services{background:linear-gradient(180deg,#fff,var(--blue-5))}
.hex{position:absolute;width:170px;height:190px;clip-path:polygon(50% 0,100% 25%,100% 75%,50% 100%,0 75%,0 25%);background:linear-gradient(160deg,#3b3f9a,var(--photo-dark) 55%,#1a6cc0)}
.hex span{position:absolute;left:0;right:0;top:112px;height:22px;background:var(--blue);color:#fff;font-size:10px;font-weight:700;display:flex;align-items:center;justify-content:center}

/* about */
.about h2{position:absolute;left:60px;top:70px;font-size:44px;font-weight:700}
.about .copy{position:absolute;left:60px;top:140px;width:440px;font-size:12px;color:var(--text);line-height:1.55}
.about .copy p+p{margin-top:14px}
.about .photo{left:560px;top:70px;width:380px;height:380px;border-radius:6px}
.about .caption{position:absolute;left:560px;top:420px;width:380px;height:40px;background:var(--blue);color:#fff;font-size:13px;font-weight:700;display:flex;align-items:center;padding-left:20px;border-radius:0 0 6px 6px}

/* financial */
.icon-strip{position:absolute;left:82px;top:128px;width:40px;height:320px;background:var(--blue);display:flex;flex-direction:column;justify-content:space-around;align-items:center}
.icon-strip i{width:18px;height:18px;border-radius:50%;border:2px solid #fff;display:block}
.fin-col{position:absolute;top:128px;width:240px}
.fin-col.featured{outline:2px solid var(--blue-3);outline-offset:4px}
.fin-col h3{height:30px;background:var(--blue);color:#fff;font-size:11px;font-weight:700;display:flex;align-items:center;justify-content:center}
.fin-col li{list-style:none;height:36px;font-size:11px;color:var(--text);display:flex;align-items:center;justify-content:center;border-bottom:1px solid #e2e6ea}
.fin-col li:nth-child(odd){background:var(--blue-5)}
.fin-col .total{height:42px;display:flex;align-items:center;justify-content:center;font-size:15px;font-weight:700}

/* event types */
.types .photo{left:0;top:0;width:470px;height:540px}
.types h2{position:absolute;left:520px;top:60px;width:440px;font-size:40px;font-weight:700;line-height:1.05}
.type-item{position:absolute;left:520px;width:420px;padding-left:52px}
.type-item b{position:absolute;left:0;top:0;width:38px;height:38px;border-radius:50%;background:var(--blue);color:#fff;font-size:13px;display:flex;align-items:center;justify-content:center}
.type-item h4{font-size:16px;font-weight:700;line-height:20px}
.type-item p{font-size:11px;color:var(--text);line-height:1.45;margin-top:6px}

/* contact */
.contact .brand{position:absolute;left:60px;top:70px}
.contact h2{position:absolute;left:60px;top:210px;font-size:44px;font-weight:700}
.contact-item{position:absolute;left:60px;width:380px;padding-left:48px}
.contact-item .ico{position:absolute;left:0;top:0;width:34px;height:34px;border-radius:50%;background:var(--blue)}
.contact-item h4{font-size:14px;font-weight:700}
.contact-item p{font-size:11px;color:var(--text);margin-top:3px}
.contact .photo{left:510px;top:0;width:490px;height:540px}
.contact .accent{position:absolute;left:490px;top:0;width:20px;height:540px;background:var(--blue)}
</style>
</head>
<body>
<main class="deck">

  <section class="slide cover">
    <div class="photo" role="img" aria-label="Conference ballroom with stage, video screens and blue lighting"></div>
    <div class="brand">KRM</div>
    <div class="intro">
      <h2>Welcome To</h2>
      <h1>Kestrel Resonance Media</h1>
      <p>Leaders in AV Production Event Design and<br>Planning &amp; Execution</p>
    </div>
    <div class="next"></div>
    <div class="bar"></div>
  </section>

  <section class="slide services">
    <h2 class="slide-title">Our Event Services</h2>
    <div class="hex" style="left:151px;top:110px" role="img" aria-label="Stage production"><span>Conference Audio Support</span></div>
    <div class="hex" style="left:327px;top:110px" role="img" aria-label="Video wall"><span>Video Wall Staging</span></div>
    <div class="hex" style="left:503px;top:110px" role="img" aria-label="Lighting rig"><span>Concert Lighting Design</span></div>
    <div class="hex" style="left:679px;top:110px" role="img" aria-label="Keynote stage"><span>Keynote Production</span></div>
    <div class="hex" style="left:239px;top:258px" role="img" aria-label="Award ceremony"><span>Award Ceremony Events</span></div>
    <div class="hex" style="left:415px;top:258px" role="img" aria-label="Live stream"><span>Live Streaming Setup</span></div>
    <div class="hex" style="left:591px;top:258px" role="img" aria-label="Trade show booth"><span>Trade Show Booths</span></div>
    <footer class="slide-footer"><span>© Copyright 2022 - All Rights Reserved</span><span>Page 02 / 06</span></footer>
  </section>

  <section class="slide about">
    <h2>About Us</h2>
    <div class="copy">
      <p>At KRM, we are passionate about live events. Our production team brings every detail to life, from the first plan to the final cue. We deliver sound, video and lighting that keep audiences engaged, with crews who know how to work under pressure and adapt quickly on any stage.</p>
      <p>With an average of fifteen years in the field, our people have supported meetings, launches and galas of every size. We treat every client as a partner and every show as our own, so your message reaches each seat in the room.</p>
    </div>
    <div class="photo" role="img" aria-label="Technician working at an audio mixing console"></div>
    <div class="caption">Average 15+ years Experience in the AV Industry</div>
    <footer class="slide-footer"><span>© Copyright 2022 - All Rights Reserved</span><span>Page 03 / 06</span></footer>
  </section>

  <section class="slide financial">
    <h2 class="slide-title">Our Entering Financial</h2>
    <div class="icon-strip"><i></i><i></i><i></i><i></i><i></i><i></i><i></i></div>
    <div class="fin-col" style="left:140px">
      <h3>Add your package title here</h3>
      <ul><li>Lorem ipsum dolor sit amet</li><li>Lorem ipsum dolor sit amet</li><li>Lorem ipsum dolor sit amet</li><li>Lorem ipsum dolor sit amet</li><li>Lorem ipsum dolor sit amet</li><li>Lorem ipsum dolor sit amet</li><li>Lorem ipsum dolor sit amet</li></ul>
      <div class="total">$ 95,00</div>
    </div>
    <div class="fin-col featured" style="left:400px">
      <h3>Add your package title here</h3>
      <ul><li>Lorem ipsum dolor sit amet</li><li>Lorem ipsum dolor sit amet</li><li>Lorem ipsum dolor sit amet</li><li>Lorem ipsum dolor sit amet</li><li>Lorem ipsum dolor sit amet</li><li>Lorem ipsum dolor sit amet</li><li>Lorem ipsum dolor sit amet</li></ul>
      <div class="total">$ 75,00</div>
    </div>
    <div class="fin-col" style="left:660px">
      <h3>Add your package title here</h3>
      <ul><li>Lorem ipsum dolor sit amet</li><li>Lorem ipsum dolor sit amet</li><li>Lorem ipsum dolor sit amet</li><li>Lorem ipsum dolor sit amet</li><li>Lorem ipsum dolor sit amet</li><li>Lorem ipsum dolor sit amet</li><li>Lorem ipsum dolor sit amet</li></ul>
      <div class="total">$ 95,00</div>
    </div>
    <footer class="slide-footer"><span>© Copyright 2022 - All Rights Reserved</span><span>Page 04 / 06</span></footer>
  </section>

  <section class="slide types">
    <div class="photo" role="img" aria-label="Ballroom set for a corporate event with stage lighting"></div>
    <h2>Types of Corporate Events Services</h2>
    <div class="type-item" style="top:180px"><b>01</b><h4>Corporate Sales Meetings</h4><p>Clear sound, bright screens and steady lighting that keep your sales team focused on goals, results and the year ahead.</p></div>
    <div class="type-item" style="top:280px"><b>02</b><h4>Advisory Board Meetings</h4><p>Discreet, reliable support for smaller rooms, with microphones, displays and remote links that let every voice be heard.</p></div>
    <div class="type-item" style="top:380px"><b>03</b><h4>Trade Shows</h4><p>Booth video walls, speaker arrays and lighting that draw visitors in and help your brand stand out on a busy floor.</p></div>
    <footer class="slide-footer"><span>© Copyright 2022 - All Rights Reserved</span><span>Page 05 / 06</span></footer>
  </section>

  <section class="slide contact">
    <div class="brand">KRM</div>
    <h2>Thank You</h2>
    <div class="contact-item" style="top:300px"><span class="ico"></span><h4>Location</h4><p>48 Harbor Light Avenue, Suite 210, Marlow Bay</p></div>
    <div class="contact-item" style="top:360px"><span class="ico"></span><h4>Contact Number</h4><p>+1 (555) 014-2290</p></div>
    <div class="contact-item" style="top:420px"><span class="ico"></span><h4>Fax</h4><p>+1 (555) 014-2291</p></div>
    <div class="accent"></div>
    <div class="photo" role="img" aria-label="Presenter on stage in front of a large video wall"></div>
    <footer class="slide-footer"><span>© Copyright 2022 - All Rights Reserved</span><span>Page 06 / 06</span></footer>
  </section>

</main>
</body>
</html>
```